Jewelers Website

This is for the DESIGN ONLY.
I am a software programmer and will be doing the development.
New website design for
www.lunagemcraft.com.au
Need a fresh new look for an online only jewellery business who produce their jewellery by hand. I would like it designed in a parallax style. Feel free to recommend fonts to use for the site. This is an Australian based company located in NSW so shots of sites in NSW might make nice background images.
http://plaxorin.me/demo/#theme=parallax
To contain the below sections
About Us
Contact Us
Gallery
Testimonials
Diamond Types
The colour scheme is to be Black / White and Silver.
With the Parallax style there will be moving sections and images for added impact.
Target Market(s)
Young Adults mainly engagement jewellery

```html
<!DOCTYPE html>
<html lang="en">
<head>
<meta charset="utf-8">
<title>Luna Gemcraft – Diamond Engagement Rings &amp; Jewellery</title>
<link href="https://fonts.googleapis.com/css2?family=Cinzel:wght@400&family=Open+Sans:wght@400;600&display=swap" rel="stylesheet">
<style>
:root{
  --nav-bg:#1c1c1c;
  --nav-line:#2e2e2e;
  --white:#ffffff;
  --paper:#e7e7e5;
  --ink:#1a1a1a;
  --text:#3a3a3a;
  --black-band:#0b0b0b;
  --card-border:#2c2c2c;
  --serif:'Cinzel', serif;
  --sans:'Open Sans', sans-serif;
}
*{box-sizing:border-box;margin:0;padding:0}
html,body{width:1200px;height:3333px;overflow:hidden}
body{background:var(--paper);font-family:var(--sans);color:var(--text);position:relative}

/* Navigation */
.site-nav{position:absolute;top:0;left:0;width:1200px;height:93px;background:var(--nav-bg);display:flex;align-items:center;z-index:2}
.brand{margin-left:40px;width:200px;font-family:var(--serif);color:var(--white);font-size:22px;line-height:24px;letter-spacing:1px}
.menu{display:flex;margin-left:auto;height:93px}
.menu a{display:flex;align-items:center;padding:0 22px;border-left:1px solid var(--nav-line);color:var(--white);text-decoration:none;font-family:var(--serif);font-size:15px;letter-spacing:.5px}
.menu-toggle{display:flex;align-items:center;justify-content:center;width:90px;border-left:1px solid var(--nav-line)}

/* Hero */
.hero{position:absolute;top:93px;left:0;width:1200px;height:611px;overflow:hidden}
.hero-photo{position:absolute;inset:0;background:
  radial-gradient(ellipse 420px 520px at 300px 380px,rgba(238,232,226,.95),rgba(238,232,226,0) 70%),
  radial-gradient(ellipse 300px 200px at 620px 380px,rgba(214,176,160,.55),rgba(214,176,160,0) 70%),
  linear-gradient(100deg,#6b5f57 0%,#b6aaa1 18%,#d9d1ca 34%,#a2948a 52%,#5e524a 70%,#3f3630 100%)}
.hero-copy{position:absolute;left:672px;top:150px;width:490px;color:var(--white);text-align:center}
.hero-kicker{display:flex;align-items:center;gap:14px;font-family:var(--serif);font-size:16px;letter-spacing:1px}
.hero-kicker::before,.hero-kicker::after{content:"";flex:1;height:2px;background:var(--white)}
.hero-title{font-family:var(--serif);font-weight:400;font-size:38px;line-height:46px;margin-top:18px}
.hero-actions{display:flex;justify-content:center;gap:10px;margin-top:18px;margin-left:-10px}
.btn-outline{display:flex;align-items:center;gap:10px;height:40px;padding:0 10px 0 26px;border:2px solid var(--white);border-radius:20px;font-family:var(--serif);font-size:14px;color:var(--white)}
.social-dot{width:40px;height:40px;border:2px solid var(--white);border-radius:50%;display:flex;align-items:center;justify-content:center}
.social-dot::after{content:"";width:10px;height:10px;border-radius:50%;background:var(--white)}
.hero-dots{position:absolute;right:40px;bottom:58px;display:flex;gap:6px;align-items:center}
.hero-dots span{width:12px;height:12px;border-radius:50%;background:rgba(255,255,255,.55)}
.hero-dots span.active{width:16px;height:16px;background:var(--white)}

/* Section headings */
.section-title{position:absolute;left:0;width:1200px;text-align:center;font-family:var(--serif);font-weight:400;font-size:31px;color:var(--ink);letter-spacing:1px}
.divider{position:absolute;left:510px;width:180px;height:40px}

/* Gallery */
.gallery{position:absolute;top:929px;left:40px;width:1118px;height:478px;display:grid;grid-template-columns:repeat(4,271px);grid-template-rows:233px 234px;column-gap:11px;row-gap:11px}
.tile{position:relative;overflow:hidden}
.tile.tall{grid-column:4;grid-row:1 / span 2}
.tile-photo{position:absolute;inset:0}
.tone-a{background:radial-gradient(circle at 30% 35%,#ffffff 0,#c9ced4 35%,#8e959c 60%,#eef0f2 100%)}
.tone-b{background:radial-gradient(circle at 45% 45%,#f4f4f4,#a3a3a3 45%,#5a5a5a 100%)}
.tone-c{background:radial-gradient(ellipse at 45% 65%,#e2e2e2 0,#8a8a8a 30%,#1e1e1e 75%)}
.tone-d{background:radial-gradient(circle at 50% 50%,#6e6e6e,#0e0e0e 70%)}
.tone-e{background:radial-gradient(ellipse 90px 140px at 50% 32%,#e8e8e8,rgba(232,232,232,0) 80%),linear-gradient(90deg,#2e3835,#6f7a77 40%,#5b6663 60%,#1f2826)}
.tile-label{position:absolute;left:0;right:0;bottom:0;height:60px;background:rgba(0,0,0,.45);color:var(--white);font-family:var(--serif);font-size:17px;display:flex;align-items:center;justify-content:center}

/* Testimonial */
.testimonial-text{position:absolute;top:1625px;left:70px;width:1060px;text-align:center;font-size:14.5px;line-height:22px;color:var(--text)}
.slider-arrow{position:absolute;width:32px;height:32px;border-radius:50%;background:#444;display:flex;align-items:center;justify-content:center}
.slider-photo{position:absolute;top:1724px;left:489px;width:222px;height:147px;background:radial-gradient(ellipse 60px 70px at 40% 40%,#3a2e2a,rgba(58,46,42,0) 80%),linear-gradient(120deg,#cfcfcf,#2e2e2e 40%,#f2f2f2 68%,#6a6a6a)}
.learn-more{position:absolute;top:1900px;left:0;width:1200px;text-align:center;font-size:16px;color:var(--ink);text-decoration:underline}

/* Diamond types */
.types{position:absolute;top:2031px;left:0;width:1200px;height:765px;background:radial-gradient(ellipse at 50% 45%,#1c1c1c,var(--black-band) 70%)}
.types .section-title{color:var(--white);top:142px}
.types-sub{position:absolute;top:200px;width:1200px;text-align:center;color:var(--white);font-size:18px}
.type-cards{position:absolute;top:351px;left:333px;display:flex;gap:13px}
.type-card{width:96px;height:180px;border:1px solid var(--card-border);padding:3px;text-align:center}
.type-image{width:88px;height:88px;background:var(--white);display:flex;align-items:center;justify-content:center}
.gem{width:62px;height:62px}
.gem-white{border-radius:50%;background:radial-gradient(circle,#ffffff,#9a9a9a)}
.gem-pink{border-radius:45%;background:radial-gradient(circle,#ffd0e2,#e0468a)}
.gem-champagne{border-radius:50% 50% 50% 50% / 40% 40% 60% 60%;background:radial-gradient(circle,#d9a86b,#6e4a22)}
.gem-simulated{width:52px;border-radius:6px;background:linear-gradient(135deg,#f4f4f8,#aeb4c4)}
.gem-synthetic{border-radius:50%;background:radial-gradient(circle,#eaf2f7,#8aa2b4)}
.type-name{margin-top:20px;color:var(--white);font-size:12.5px;line-height:16px}
.btn-small{position:absolute;top:594px;left:564px;width:72px;height:24px;border:1px solid #555;border-radius:12px;color:var(--white);font-size:10px;display:flex;align-items:center;justify-content:center}

/* Map */
.map{position:absolute;top:2796px;left:0;width:1200px;height:315px}
.map-area{position:absolute;inset:0;background:
  radial-gradient(ellipse 260px 120px at 1000px 40px,#a6c8e6,rgba(166,200,230,0) 80%),
  radial-gradient(ellipse 200px 90px at 900px 140px,#a9cbe6,rgba(169,203,230,0) 80%),
  linear-gradient(90deg,#e9e2c8,#ede4c2 40%,#dfe2c6 62%,#c6d9e4 82%,#aacbe4)}
.map-tabs{position:absolute;top:42px;left:40px;display:flex;background:var(--white);border-radius:20px;height:40px}
.map-tabs span{display:flex;align-items:center;justify-content:center;width:108px;font-size:14px;color:var(--ink);border-radius:20px}
.map-tabs span.active{background:var(--ink);color:var(--white)}
.map-pin{position:absolute;left:755px;top:92px}
.map-info{position:absolute;bottom:0;left:0;width:1200px;height:33px;background:rgba(255,255,255,.85);display:flex;align-items:center;padding:0 40px;font-size:13px;color:var(--ink);gap:40px}
.map-info span{display:flex;align-items:center;gap:6px}
.map-info .btn-map{margin-left:auto;border:1px solid #555;border-radius:12px;height:20px;padding:0 16px;font-size:11px}

/* Footer */
.site-footer{position:absolute;top:3111px;left:0;width:1200px;height:222px;text-align:center;color:var(--ink)}
.copyright{margin-top:50px;font-size:12px}
.footer-links{margin-top:10px;font-size:12px}
.footer-links a{color:var(--ink);text-decoration:none}
.footer-social{display:flex;justify-content:center;gap:10px;margin-top:22px}
.footer-social span{width:36px;height:36px;border:2px solid #888;border-radius:50%;display:flex;align-items:center;justify-content:center}
.footer-social span::after{content:"";width:9px;height:9px;border-radius:50%;background:#888}
</style>
</head>
<body>

<header class="site-nav">
  <div class="brand">LUNA<br>GEMCRAFT</div>
  <nav class="menu">
    <a href="#about">ABOUT US</a>
    <a href="#contact">CONTACT US</a>
    <a href="#gallery">GALLERY</a>
    <a href="#testimonials">TESTIMONIALS</a>
    <a href="#types">DIAMOND TYPES</a>
    <span class="menu-toggle"><svg width="24" height="18" viewBox="0 0 24 18"><rect y="1" width="24" height="3" fill="#fff"/><rect y="8" width="24" height="3" fill="#fff"/><rect y="15" width="24" height="3" fill="#fff"/></svg></span>
  </nav>
</header>

<section class="hero">
  <div class="hero-photo" role="img" aria-label="Bride in a jewelled white gown slipping a diamond ring onto her finger"></div>
  <div class="hero-copy">
    <div class="hero-kicker">WELCOME TO LUNA GEMCRAFT</div>
    <h1 class="hero-title">DIAMOND ENGAGEMENT<br>RINGS &amp; JEWELLERY</h1>
    <div class="hero-actions">
      <span class="btn-outline">CALL TO ACTION <svg width="22" height="22" viewBox="0 0 22 22"><circle cx="11" cy="11" r="10" fill="none" stroke="#fff" stroke-width="1.5"/><path d="M9 6l5 5-5 5" fill="none" stroke="#fff" stroke-width="1.5"/></svg></span>
      <span class="social-dot" aria-label="Social link"></span><span class="social-dot" aria-label="Social link"></span><span class="social-dot" aria-label="Social link"></span>
    </div>
  </div>
  <div class="hero-dots"><span></span><span class="active"></span><span></span></div>
</section>

<h2 class="section-title" id="gallery" style="top:800px">DIAMONDS GALLERY</h2>
<svg class="divider" style="top:845px" viewBox="0 0 180 40"><rect x="0" y="18" width="180" height="4" fill="#111"/><circle cx="90" cy="20" r="16" fill="#111"/><rect x="82" y="15" width="16" height="11" rx="2" fill="#fff"/><circle cx="90" cy="20.5" r="3" fill="#111"/></svg>

<div class="gallery">
  <figure class="tile"><div class="tile-photo tone-a" role="img" aria-label="Scattered loose diamonds on white"></div><figcaption class="tile-label">Lorem Ipsum</figcaption></figure>
  <figure class="tile"><div class="tile-photo tone-b" role="img" aria-label="Single diamond close-up on grey"></div><figcaption class="tile-label">Lorem Ipsum</figcaption></figure>
  <figure class="tile"><div class="tile-photo tone-a" role="img" aria-label="Scattered loose diamonds on white"></div><figcaption class="tile-label">Lorem Ipsum</figcaption></figure>
  <figure class="tile tall"><div class="tile-photo tone-e" role="img" aria-label="Solitaire diamond ring close-up"></div><figcaption class="tile-label">Lorem Ipsum</figcaption></figure>
  <figure class="tile"><div class="tile-photo tone-c" role="img" aria-label="Diamonds on a dark reflective surface"></div><figcaption class="tile-label">Lorem Ipsum</figcaption></figure>
  <figure class="tile"><div class="tile-photo tone-d" role="img" aria-label="Many small diamonds on black"></div><figcaption class="tile-label">Lorem Ipsum</figcaption></figure>
  <figure class="tile"><div class="tile-photo tone-c" role="img" aria-label="Diamonds on a dark reflective surface"></div><figcaption class="tile-label">Lorem Ipsum</figcaption></figure>
</div>

<h2 class="section-title" id="testimonials" style="top:1530px">DANIEL &amp; SIENNA</h2>
<svg class="divider" style="top:1577px" viewBox="0 0 180 40"><rect x="0" y="18" width="180" height="4" fill="#111"/><circle cx="90" cy="20" r="16" fill="#111"/><path d="M82 24c0-5 2-8 5-9v3c-1 1-2 2-2 3h2v5h-5zM91 24c0-5 2-8 5-9v3c-1 1-2 2-2 3h2v5h-5z" fill="#fff"/></svg>
<p class="testimonial-text">Daniel and I met at a mutual friend's 16th&nbsp; Birthday Party in 2005. We immediately became good friends and by June 2006 we were officially dating. Daniel and I also went to school next door to each other so we got through the stresses of year 11 and 12 together. Daniel proposed to me in December 2010 at my favourite picnic...</p>
<span class="slider-arrow" style="top:1782px;left:433px"><svg width="12" height="12" viewBox="0 0 12 12"><path d="M8 1L3 6l5 5" fill="none" stroke="#fff" stroke-width="2"/></svg></span>
<div class="slider-photo" role="img" aria-label="Engaged couple embracing in wedding attire"></div>
<span class="slider-arrow" style="top:1782px;left:735px"><svg width="12" height="12" viewBox="0 0 12 12"><path d="M4 1l5 5-5 5" fill="none" stroke="#fff" stroke-width="2"/></svg></span>
<a class="learn-more" href="#testimonials">Learn More</a>

<section class="types" id="types">
  <h2 class="section-title">DIAMOND TYPES</h2>
  <p class="types-sub">Choosing the cut and shape of Diamond</p>
  <svg class="divider" style="top:267px" viewBox="0 0 180 40"><rect x="0" y="18" width="180" height="4" fill="#fff"/><circle cx="90" cy="20" r="13" fill="#fff"/><circle cx="90" cy="20" r="7" fill="#0b0b0b"/></svg>
  <div class="type-cards">
    <div class="type-card"><div class="type-image"><div class="gem gem-white" role="img" aria-label="White diamond"></div></div><p class="type-name">White<br>Diamonds</p></div>
    <div class="type-card"><div class="type-image"><div class="gem gem-pink" role="img" aria-label="Pink diamond"></div></div><p class="type-name">Pink<br>Diamonds</p></div>
    <div class="type-card"><div class="type-image"><div class="gem gem-champagne" role="img" aria-label="Champagne diamond"></div></div><p class="type-name">Champagne<br>Diamonds</p></div>
    <div class="type-card"><div class="type-image"><div class="gem gem-simulated" role="img" aria-label="Simulated diamond"></div></div><p class="type-name">Simulated<br>Diamonds</p></div>
    <div class="type-card"><div class="type-image"><div class="gem gem-synthetic" role="img" aria-label="Synthetic diamond"></div></div><p class="type-name">Synthetic<br>Diamonds</p></div>
  </div>
  <span class="btn-small">Click Here</span>
</section>

<section class="map" id="contact">
  <div class="map-area" role="img" aria-label="Street map of Sydney and surrounding suburbs"></div>
  <div class="map-tabs"><span class="active">Sydney</span><span>Germany</span></div>
  <svg class="map-pin" width="32" height="44" viewBox="0 0 32 44"><path d="M16 0C7 0 0 7 0 16c0 12 16 28 16 28s16-16 16-28C32 7 25 0 16 0z" fill="#111"/><circle cx="16" cy="15" r="6" fill="#fff"/></svg>
  <div class="map-info">
    <span><svg width="10" height="14" viewBox="0 0 10 14"><path d="M5 0C2 0 0 2 0 5c0 4 5 9 5 9s5-5 5-9c0-3-2-5-5-5z" fill="#111"/><circle cx="5" cy="5" r="2" fill="#fff"/></svg>Marlow Vale NSW 2299, Australia</span>
    <span><svg width="13" height="13" viewBox="0 0 13 13"><path d="M3 0l2 3-1.5 1.5c1 2 3 4 5 5L10 8l3 2-1.5 3C6 13 0 7 0 1.5z" fill="#111"/></svg>+61 (0)2 9000 4821</span>
    <span class="btn-map">Click Here</span>
  </div>
</section>

<footer class="site-footer" id="about">
  <p class="copyright">© Copyright 2014 Luna Gemcraft Pty Ltd</p>
  <p class="footer-links"><a href="#about">About Us</a> - <a href="#contact">Contact Us</a> - <a href="#gallery">Gallery</a> - <a href="#testimonials">Testimonials</a> - <a href="#types">Diamond Types</a></p>
  <div class="footer-social"><span aria-label="Social link"></span><span aria-label="Social link"></span><span aria-label="Social link"></span></div>
</footer>

</body>
</html>
```